Website design for SaaS -solution

We are B2B SaaS company. (Korlet.io) Our software brings leads by enriching company profiles with external data. We want to take load off from marketing and sales directors by bringing them sales leads.

Our core values that we want to communicate:
-Data driven
-Easy going and easy to use
-Sincere and honest
-Humble
-lively

We would like to see designs that obey our colours (logos attached) but also the website should be lively and visual / photo intensive. We only use few sentences to power our message. Here are few examples:

http://www.plovista.com/
https://www.zundel.com/

We will also make a video that we post in the front cover. Our current website is www.korlet.io. The font we would like to use is Avenir Next or similar

• Avenir Next

0455a3
ec1f27
9bcb3c
85acd3

• 1 page: the main page (attached is brief) (This is most important one)
• 2. page: , a design where we can post content such as slides, e-papers etc (e.g.. http://www.brightmoor.com/eu/industries/)
• 3. page: a basic template that can be used for various needs ( team-page, jobs, page, etc)

```html
<!DOCTYPE html>
<html lang="en">
<head>
<meta charset="utf-8">
<title>Korlet — B2B sales leads</title>
<link rel="stylesheet" href="https://fonts.googleapis.com/css2?family=Mulish:wght@400;600;700&family=Arimo:wght@400;700&display=swap">
<style>
:root{
  --blue:#0a52a2;
  --blue-dark:#06458c;
  --panel:rgba(10,82,162,.92);
  --ink:#2f2f2f;
  --grey-band:#d6d6d6;
  --btn-grey:#dedede;
  --footer-bar:#2b2b2b;
  --white:#ffffff;
  --link:#9fd0ff;
}
*{box-sizing:border-box;margin:0;padding:0}
html,body{width:743px;height:1200px;overflow:hidden;background:var(--white)}
body{position:relative;font-family:"Arimo",Arial,sans-serif;color:var(--ink)}
.abs{position:absolute}
.heading{font-family:"Mulish","Avenir Next",sans-serif}

/* top bar */
.topbar{left:0;top:0;width:743px;height:26px;background:var(--blue)}
.social-top{left:89px;top:7px;display:flex;gap:4px}
.social-top span{width:13px;height:13px;background:#6fa6de;border-radius:2px;display:block}
.toplinks{right:93px;top:8px;font-size:8px;color:var(--white);display:flex;gap:16px}

/* header */
.header{left:0;top:26px;width:743px;height:55px;background:var(--white)}
.brand{left:86px;top:40px;display:flex;align-items:center;gap:8px}
.brand-dot{width:22px;height:22px;border-radius:50%;background:var(--blue)}
.brand-name{font-family:"Mulish",sans-serif;font-size:30px;font-weight:600;color:#9a9a9a;line-height:1}
.nav{left:334px;top:26px;display:flex;height:55px;font-family:"Mulish",sans-serif;font-size:8.5px;font-weight:600;color:#333}
.nav a{display:flex;align-items:center;padding:0 15px;text-decoration:none;color:inherit}
.nav a.active{background:#ececec;border-bottom:2px solid #9ab7d6}

/* hero */
.hero{left:0;top:81px;width:743px;height:302px;background:linear-gradient(100deg,#4a4540 0%,#6d6a66 30%,#8d8a86 55%,#b8b3ab 80%,#d9cdb8 100%)}
.hero-panel{left:437px;top:81px;width:220px;height:302px;background:var(--panel);color:var(--white)}
.hero-panel h2{position:absolute;left:11px;font-size:17.5px;font-weight:600}
.hero-panel p{position:absolute;left:13px;width:198px;font-size:9.2px;line-height:13.6px}
.hero-panel .divider{position:absolute;left:0;top:163px;width:220px;height:1px;background:rgba(255,255,255,.25)}
.btn-grey{position:absolute;left:137px;width:69px;height:23px;background:var(--btn-grey);color:#222;font-family:"Mulish",sans-serif;font-weight:700;font-size:8.5px;display:flex;align-items:center;justify-content:center}

/* signup band */
.signup{left:0;top:383px;width:743px;height:67px;background:var(--grey-band)}
.signup-input{left:212px;top:406px;width:222px;height:25px;background:var(--white);font-size:8px;color:#999;padding:8px 10px}
.signup-btn{left:440px;top:406px;width:57px;height:25px;background:var(--blue);color:var(--white);font-family:"Mulish",sans-serif;font-weight:700;font-size:10.5px;display:flex;align-items:center;justify-content:center}

/* features */
.section-title{left:0;width:743px;text-align:center;font-size:17px;font-weight:700;color:#333}
.section-sub{left:0;top:505px;width:743px;text-align:center;font-size:8.3px;color:#444}
.feature{top:553px;width:160px;text-align:center}
.feature svg{display:block;margin:0 auto}
.feature-label{margin-top:20px;font-family:"Mulish",sans-serif;font-size:14.5px;font-weight:600;color:#333;letter-spacing:.3px}

/* testimonials */
.testimonials{left:0;top:696px;width:743px;height:260px;background:linear-gradient(180deg,#dcdcdc 0%,#e9e9e9 45%,#cfd6dd 100%)}
.quote{left:76px;top:826px;width:592px;text-align:center;font-family:"Mulish",sans-serif;font-size:8.8px;line-height:13.6px;color:#222}
.written{left:0;top:881px;width:743px;text-align:center;font-family:"Mulish",sans-serif;font-size:8px;font-weight:700;color:#222;line-height:14px}
.dots{left:301px;top:926px;display:flex;gap:2px}
.dots span{width:21px;height:3px;background:var(--white)}
.dots span.on{background:var(--blue)}

/* footer */
.footer{left:0;top:956px;width:743px;height:188px;background:var(--blue);color:var(--white)}
.footer h4{position:absolute;top:22px;font-family:"Mulish",sans-serif;font-size:11px;font-weight:700}
.contact-item{position:absolute;left:83px;display:flex;gap:6px;font-size:7.8px;line-height:10px}
.contact-item svg{flex:none}
.tweet{position:absolute;left:236px;width:125px;font-size:7px;line-height:9.2px}
.tweet b{font-size:7.3px}
.tweet .handle{color:#a9c8ea;font-size:6px}
.tweet .url{color:var(--link)}
.about-list{position:absolute;left:383px;top:46px;font-size:7.6px;line-height:17.1px;list-style:none}
.follow-text{position:absolute;left:522px;top:46px;width:133px;font-size:7.6px;line-height:11.4px;text-align:justify}
.follow-icons{position:absolute;left:523px;top:112px;display:flex;gap:6px}
.follow-icons span{width:17px;height:17px;background:#c9c9c9;display:block}
.footer-brand{position:absolute;left:548px;top:143px;display:flex;align-items:center;gap:6px}
.footer-brand .brand-dot{width:14px;height:14px;background:#9bb9dc}
.footer-brand .brand-name{font-size:20px;color:#b9cde4}
.bottombar{left:0;top:1144px;width:743px;height:33px;background:var(--footer-bar);color:var(--white);font-size:8px}
.bottombar .copy{position:absolute;left:83px;top:12px}
.bottombar .legal{position:absolute;right:89px;top:12px}
</style>
</head>
<body>

<div class="abs topbar"></div>
<div class="abs social-top" aria-label="Social links"><span></span><span></span><span></span><span></span><span></span><span></span></div>
<div class="abs toplinks"><span>Login</span><span>|</span><span>Blog</span><span>|</span><span>Contact</span><span>|</span><span>+1.800.555.0142</span><span>|</span><span>Americas (English)</span></div>

<header class="abs header"></header>
<div class="abs brand"><span class="brand-dot"></span><span class="brand-name">korlet</span></div>
<nav class="abs nav"><a class="active">HOME</a><a>TEAM</a><a>PRODUCTS</a><a>CUSTOMER</a><a>CAREERS</a></nav>

<div class="abs hero" role="img" aria-label="Photo of business people around a laptop showing a bar chart, with coffee and notepad"></div>
<section class="abs hero-panel">
  <h2 class="heading" style="top:18px">What Korlet is</h2>
  <p style="top:46px">We go through open data and identify with prospective purchase behavior signals. We gather every day a huge amount of information that organizations focus our right and we value their sales potential perspective.</p>
  <div class="btn-grey" style="top:128px">Learn More</div>
  <div class="divider"></div>
  <h2 class="heading" style="top:173px">Engage Everywhere</h2>
  <p style="top:202px">We go through open data and identify with prospective purchase behavior signals. We gather every day a huge amount</p>
  <div class="btn-grey" style="top:256px">Learn More</div>
</section>

<div class="abs signup"></div>
<div class="abs signup-input">Enter Your Business Mail</div>
<div class="abs signup-btn">Submit</div>

<h2 class="abs section-title heading" style="top:474px">Is B2B sales completely gone digital?</h2>
<p class="abs section-sub">Lorem Ipsum is simply dummy text of the printing and typesetting industry Ipsum has been the industry's standard dummy text</p>

<div class="abs feature" style="left:98px">
  <svg width="64" height="64" viewBox="0 0 64 64"><circle cx="32" cy="32" r="31" fill="var(--blue)"/><path d="M20 28h6l12-7v22l-12-7h-6z" fill="#fff"/><path d="M24 36l3 8h4l-2-8" fill="#fff"/><path d="M42 25l5-3M43 32h6M42 39l5 3" stroke="#fff" stroke-width="2" stroke-linecap="round"/></svg>
  <div class="feature-label">MARKETING</div>
</div>
<div class="abs feature" style="left:275px">
  <svg width="64" height="64" viewBox="0 0 64 64"><circle cx="32" cy="32" r="31" fill="var(--blue)"/><path d="M16 22h5l4 16h18l3-11H23" fill="none" stroke="#fff" stroke-width="2.2" stroke-linejoin="round"/><circle cx="27" cy="43" r="2.5" fill="#fff"/><circle cx="41" cy="43" r="2.5" fill="#fff"/><path d="M29 29l3 3 6-6" fill="none" stroke="#fff" stroke-width="2"/></svg>
  <div class="feature-label">SALES</div>
</div>
<div class="abs feature" style="left:448px">
  <svg width="64" height="64" viewBox="0 0 64 64"><circle cx="32" cy="32" r="31" fill="var(--blue)"/><circle cx="32" cy="35" r="11" fill="none" stroke="#fff" stroke-width="2.2"/><path d="M32 35v-6M29 20h6M32 20v4" stroke="#fff" stroke-width="2.2" stroke-linecap="round"/></svg>
  <div class="feature-label">INDUSTRY EXPERT</div>
</div>

<section class="abs testimonials" role="img" aria-label="Soft faded photo of hands with a pen over printed business charts"></section>
<h2 class="abs section-title heading" style="top:713px;font-weight:600;letter-spacing:.4px">OUR TESTIMONIALS</h2>
<svg class="abs" style="left:333px;top:756px" width="46" height="46" viewBox="0 0 46 46"><circle cx="23" cy="23" r="23" fill="var(--blue)"/><path d="M13 18h8v8l-3 7h-4l3-7h-4zM25 18h8v8l-3 7h-4l3-7h-4z" fill="#fff"/></svg>
<p class="abs quote">"Korlet help us to find new potential customers and also to deepen existing customer relationships. Scent desire to customize exactly to our needs service tool has been ihaltavaa "Korlet help us to find new potential customers and also to deepen existing customer relationships. Scent desire to customize exactly to our needs service tool has been ihaltavaa""</p>
<p class="abs written">Written By<br>AARNE KESTILÄ, SALES MANAGER, NORVEL LTD</p>
<div class="abs dots"><span class="on"></span><span></span><span></span><span></span><span></span></div>

<footer class="abs footer">
  <h4 style="left:83px">Contact us</h4>
  <div class="contact-item" style="top:47px"><svg width="11" height="11" viewBox="0 0 12 12"><circle cx="6" cy="6" r="5.3" fill="none" stroke="#fff"/><path d="M4 3.5l1 1.5-.6.8 1.8 1.8.8-.6 1.5 1-.7 1C6 9 3 6 3.2 4.2z" fill="#fff"/></svg><span>03 5550 0147 (Phone)</span></div>
  <div class="contact-item" style="top:75px"><svg width="12" height="11" viewBox="0 0 12 11"><rect x="1" y="4" width="10" height="6" fill="#fff"/><rect x="3" y="1" width="6" height="3" fill="none" stroke="#fff"/></svg><span>03 5550 0147 (Fax)</span></div>
  <div class="contact-item" style="top:103px"><svg width="11" height="9" viewBox="0 0 11 9"><rect x=".5" y=".5" width="10" height="8" fill="#fff"/><path d="M.5.5l5 4 5-4" fill="none" stroke="var(--blue)"/></svg><span>hello@korlet.io</span></div>
  <div class="contact-item" style="top:130px"><svg width="10" height="13" viewBox="0 0 10 13"><path d="M5 12C2 8 1 6 1 4.5a4 4 0 018 0C9 6 8 8 5 12z" fill="#fff"/><circle cx="5" cy="4.5" r="1.5" fill="var(--blue)"/></svg><span>PO Box : 4410, Lorem Lorem<br>ipsum dollor si2210</span></div>

  <h4 style="left:236px">Latest Feed</h4>
  <div class="tweet" style="top:46px"><b>Selma</b> <span class="handle">@driftlane</span><br>How to Download Photos from Your Feed to... <span class="url">drftl.co/Q4kzR7pLm</span></div>
  <div class="tweet" style="top:84px"><b>Selma</b> <span class="handle">@driftlane</span><br>How to Download Photos from Your Feed to... <span class="url">drftl.co/Q4kzR7pLm</span></div>
  <div class="tweet" style="top:122px"><b>Selma</b> <span class="handle">@driftlane</span><br>How to Download Photos from Your Feed to... <span class="url">drftl.co/Q4kzR7pLm</span></div>

  <h4 style="left:383px">About Us</h4>
  <ul class="about-list"><li>Investor</li><li>Careers</li><li>Terms &amp; Conditions of Services</li><li>Privacy Policy</li><li>Services Level Agreement</li><li>Master Commerical Agfrement</li></ul>

  <h4 style="left:521px">Follow Us</h4>
  <p class="follow-text">Lorem Ipsum is simply dummy text of the printing and typesetting industry. Lorem Ipsum has been the industry's standard dummy text ever since the 1500s,</p>
  <div class="follow-icons"><span></span><span></span><span></span><span></span><span></span><span></span></div>
  <div class="footer-brand"><span class="brand-dot"></span><span class="brand-name">korlet</span></div>
</footer>

<div class="abs bottombar">
  <span class="copy">© Copyright 2015, Plovista, Inc. All rights reserved.</span>
  <span class="legal">Site Map | Legal | Privacy | Cookies</span>
</div>

</body>
</html>
```